data and media shredding company needs a flyer design

We need a flyer design for a startup company based on Long Island, NY. We shred all types of storage devices at the customers location. We want to emphasize on the dangers of identity theft and confidential information. With some focus on e-waste recycling. We want to coordinate the flyer with our website design.
www.vaultmincerservices.example

Target Market(s)

business owners that have personal information that needs to be destroyed

Font styles to use
Sans Serif

Colors

Designer to choose colors to be used in the design.

Requirements
Must have
• must have company name and logo, must have web address, must have phone number 855-310-4968, must have briefing of what we do, must be set for a trifold flyer

```html
<!DOCTYPE html>
<html lang="en">
<head>
<meta charset="utf-8">
<title>Vault Mincer Services – Trifold Flyer</title>
<link rel="stylesheet" href="https://fonts.googleapis.com/css2?family=Open+Sans:wght@400;600;700;800&display=swap">
<style>
  :root {
    --page: #e6e8e4;
    --green: #7dbb2f;
    --green-light: #9dd046;
    --green-dark: #4f8a1c;
    --navy: #1c2a33;
    --ink-dark: #151d22;
    --blue: #14488f;
    --white: #ffffff;
    --text-light: #eef3ea;
  }
  * { box-sizing: border-box; margin: 0; padding: 0; }
  html, body { width: 1200px; height: 801px; overflow: hidden; }
  body {
    background: var(--page);
    font-family: "Open Sans", Arial, sans-serif;
    position: relative;
  }
  .trifold {
    position: absolute; left: 30px; top: 30px;
    width: 1140px; height: 741px;
    display: flex;
    box-shadow: 0 8px 24px rgba(0,0,0,.18);
  }
  .panel { position: relative; width: 380px; height: 741px; overflow: hidden; }
  .panel-bg { position: absolute; inset: 0; width: 100%; height: 100%; }
  .panel-content { position: absolute; inset: 0; padding: 36px 30px; }

  .heading { font-weight: 800; text-transform: uppercase; line-height: 1.1; }
  .body-copy {
    font-size: 10.5px; line-height: 1.55; text-transform: uppercase;
    text-align: justify; letter-spacing: .2px;
  }

  /* Left panel */
  .about .heading { color: var(--white); font-size: 15px; margin-bottom: 8px; }
  .about .body-copy { color: var(--text-light); }
  .hard-drive { position: absolute; left: 30px; right: 30px; top: 400px; }
  .hard-drive .heading { color: var(--white); font-size: 15px; margin-bottom: 8px; }
  .hard-drive .body-copy { color: var(--white); margin-bottom: 14px; }

  /* Middle panel */
  .services-title {
    color: var(--blue); font-size: 24px; text-align: right;
    margin: 6px 0 40px;
  }
  .service { display: flex; gap: 12px; margin-bottom: 26px; }
  .service-icon { flex: 0 0 26px; height: 26px; margin-top: 2px; }
  .service h3 {
    color: var(--blue); font-size: 12.5px; font-weight: 800;
    text-transform: uppercase; margin-bottom: 6px; line-height: 1.2;
  }
  .service .body-copy { color: var(--white); font-size: 10px; }

  /* Cover panel */
  .brand {
    position: absolute; top: 30px; left: 0; right: 0;
    display: flex; flex-direction: column; align-items: center; gap: 6px;
  }
  .brand-dot { width: 34px; height: 34px; border-radius: 50%; border: 3px solid var(--green); }
  .brand-name { color: var(--blue); font-weight: 700; font-size: 15px; }
  .tagline {
    position: absolute; top: 175px; left: 34px; right: 34px;
    color: var(--white); text-transform: uppercase;
  }
  .tagline .small { font-size: 24px; font-weight: 600; line-height: 1.05; display: block; }
  .tagline .big { font-size: 62px; font-weight: 700; color: var(--blue); line-height: 1; display: block; }
  .hero-image { position: absolute; right: 0; top: 310px; width: 260px; height: 260px; }
  .hero-caption {
    position: absolute; right: 26px; top: 398px; width: 170px;
    color: var(--white); font-weight: 700; font-size: 15px;
    text-transform: uppercase; text-align: center; line-height: 1.35;
  }
  .contact {
    position: absolute; bottom: 30px; left: 30px; right: 30px;
    text-align: center;
  }
  .badges { display: flex; justify-content: center; gap: 14px; margin-bottom: 10px; }
  .badge-rect { width: 64px; height: 32px; background: var(--blue); border-radius: 3px; }
  .badge-circle { width: 34px; height: 34px; border-radius: 50%; background: #2b6aa5; border: 3px solid var(--green); }
  .contact h4 { color: var(--green); font-size: 20px; font-weight: 800; text-transform: uppercase; }
  .contact p { color: var(--blue); font-size: 11px; text-transform: uppercase; line-height: 1.5; }
  .contact .email { text-transform: none; }
</style>
</head>
<body>
<main class="trifold">

  <section class="panel panel-about">
    <svg class="panel-bg" viewBox="0 0 380 741" preserveAspectRatio="none" aria-hidden="true">
      <rect width="380" height="741" fill="var(--green)"/>
      <polygon points="0,0 380,0 380,60 140,420 0,420" fill="var(--navy)"/>
      <polygon points="0,300 0,520 160,420" fill="var(--ink-dark)" opacity=".85"/>
      <polygon points="0,741 380,741 380,500" fill="var(--green-dark)" opacity=".35"/>
    </svg>
    <div class="panel-content">
      <div class="about">
        <h2 class="heading">About Us</h2>
        <p class="body-copy">Vault Mincer Services was founded by Martin Hale, a longtime business owner who was born and raised on Long Island. Martin has extensive hands-on experience in the data and equipment destruction industry. As a result, he saw the need for certified on-site destruction of data media, which is not only convenient for clients but also highly secure. We provide a unique data destruction service by not only picking up your data media but actually securely destroying the data and media on your site (home or office). This provides assurance to our clients that the data in a readable form will never leave their site. We are primarily providing service to Nassau and Suffolk counties, but are available to the tri-state area.</p>
      </div>
    </div>
    <div class="hard-drive">
      <h2 class="heading">Hard Drive &amp;<br>Media Destruction</h2>
      <p class="body-copy">Erasing, degaussing, or formatting hard drives and media may leave them vulnerable for data theft as data may still remain on the drives. The only sure way to be certain that important data, confidential files, privacy information, etc. are actually destroyed is to physically shred the drive/media. We provide a unique data destruction service by not only picking up your data media, but actually securely destroying the data and media on your site.</p>
      <p class="body-copy">The media is shredded onsite in our mobile shredder trailer. We document the actual destruction with photographs and videos which are provided to each client along with a certificate of destruction listing all.</p>
    </div>
  </section>

  <section class="panel panel-services">
    <svg class="panel-bg" viewBox="0 0 380 741" preserveAspectRatio="none" aria-hidden="true">
      <rect width="380" height="741" fill="var(--green)"/>
      <polygon points="0,0 90,0 0,150" fill="var(--navy)"/>
      <polygon points="0,741 380,741 380,380 160,741" fill="var(--green-light)" opacity=".5"/>
      <polygon points="380,0 380,220 250,0" fill="var(--green-light)" opacity=".35"/>
    </svg>
    <div class="panel-content">
      <h2 class="heading services-title">Destruction<br>Services</h2>

      <article class="service">
        <svg class="service-icon" viewBox="0 0 26 26" aria-hidden="true">
          <rect x="3" y="3" width="20" height="20" rx="2" fill="none" stroke="#fff" stroke-width="1.5"/>
          <circle cx="13" cy="12" r="5" fill="none" stroke="#fff" stroke-width="1.5"/>
        </svg>
        <div>
          <h3>Commercial Hard Drive Destruction</h3>
          <p class="body-copy">Our on-site destruction services are handled by a trained professional. We provide the highest level of security and document every job with photographs and videos, plus a certificate of destruction.</p>
        </div>
      </article>

      <article class="service">
        <svg class="service-icon" viewBox="0 0 26 26" aria-hidden="true">
          <rect x="2" y="7" width="22" height="12" rx="2" fill="none" stroke="#fff" stroke-width="1.5"/>
          <line x1="6" y1="13" x2="20" y2="13" stroke="#fff" stroke-width="1.5"/>
        </svg>
        <div>
          <h3>Electronic Media Destruction</h3>
          <p class="body-copy">Erasing or degaussing often leaves information behind. We shred hard drives, tapes, CDs, DVDs, flash drives, phones and other portable storage devices so nothing can be recovered.</p>
        </div>
      </article>

      <article class="service">
        <svg class="service-icon" viewBox="0 0 26 26" aria-hidden="true">
          <path d="M6 3h10l5 5v15H6z" fill="none" stroke="#fff" stroke-width="1.5"/>
          <line x1="9" y1="13" x2="18" y2="13" stroke="#fff" stroke-width="1.5"/>
          <line x1="9" y1="17" x2="18" y2="17" stroke="#fff" stroke-width="1.5"/>
        </svg>
        <div>
          <h3>Paper &amp; Other Confidential Material</h3>
          <p class="body-copy">Vault Mincer Services can get rid of your unwanted documents and files. We are a full service that will recycle all of your confidential materials such as medical records, legal files, financials, X-rays and other sensitive documents.</p>
        </div>
      </article>
    </div>
  </section>

  <section class="panel panel-cover">
    <svg class="panel-bg" viewBox="0 0 380 741" preserveAspectRatio="none" aria-hidden="true">
      <rect width="380" height="741" fill="var(--white)"/>
      <polygon points="0,0 20,0 190,150 360,0 380,0 380,741 0,741" fill="var(--green)"/>
      <polygon points="0,600 200,585 380,600 380,741 0,741" fill="var(--white)"/>
      <polygon points="110,310 380,290 380,598 120,582" fill="var(--green-dark)"/>
    </svg>
    <div class="brand">
      <span class="brand-dot"></span>
      <span class="brand-name">Vault Mincer Services</span>
    </div>
    <h1 class="tagline">
      <span class="small">Keep your<br>information</span>
      <span class="big">Safe</span>
    </h1>
    <svg class="hero-image" viewBox="0 0 260 260" preserveAspectRatio="none" role="img" aria-label="Close-up photograph of an open hard drive platter">
      <defs>
        <radialGradient id="platter" cx="70%" cy="40%" r="75%">
          <stop offset="0" stop-color="#6e7a82"/>
          <stop offset=".6" stop-color="#2c3a44"/>
          <stop offset="1" stop-color="#151d22"/>
        </radialGradient>
      </defs>
      <polygon points="20,18 260,0 260,260 30,245" fill="url(#platter)"/>
    </svg>
    <p class="hero-caption">Certified &amp; secure complete destruction of data &amp; media</p>
    <div class="contact">
      <div class="badges">
        <span class="badge-rect"></span>
        <span class="badge-circle"></span>
      </div>
      <h4>Get in touch</h4>
      <p>Phone: 855-310-4968</p>
      <p class="email">EMAIL: info@vaultmincerservices.example</p>
    </div>
  </section>

</main>
</body>
</html>
```